Web Banners

I need banners to run ads in Chatterly and plume ads. No flash needed. Just static or animated as you see fit.

Our website: www.tidewavecourses.com
The banners will be promoting our surf camps in Kelso and Marrowby as "Harbor Retreats".

I will be using this 3rd party site to list my ads. Here are their full requirements:
http://support.bannerlift.com/creative-requirements/

These are the banners I need
- Banner – 468×60
- Square – 250×250
- Small Square – 200×200
- Leaderboard – 728×90
- Medium Rectangle – 300×250
- Large Rectangle – 336×280
- Skyscraper – 120×600
- Wide Skyscraper – 160×600
- Mobile Leaderboard – 320×50
- Chatterly – 100×72
- Chatterly News Feed – 200×200, 600×315

For proofing purposes, if you want to do 1 or 2 in the beginning, that's fine.
Once we approve your direction, I would need the remaining banners before final payment is made. I have included some graphics to get you started.

Key focus for any statements would be:
learn from pro surfers
make new friends
learn how to surf
improve your surfing skills

```html
<!DOCTYPE html>
<html lang="en">
<head>
<meta charset="utf-8">
<title>Harbor Retreats – Web Banner Set</title>
<link rel="stylesheet" href="https://fonts.googleapis.com/css2?family=Comfortaa:wght@400;700&family=Fredoka:wght@600&display=swap">
<style>
  :root {
    --page: #ffffff;
    --teal: #5fb3ad;
    --teal-light: #a9dcd6;
    --teal-dark: #3f8f8a;
    --wood: #8d877c;
    --wood-light: #b6b0a4;
    --wood-dark: #5e5a52;
    --ink: #111111;
    --badge: #1b1b1b;
    --badge-edge: #4a4a4a;
    --white: #ffffff;
    --sky: #dfeef5;
    --sea: #6fa9c4;
    --sand: #e9e2d2;
    --board: #f1df3c;
  }
  * { box-sizing: border-box; margin: 0; padding: 0; }
  html, body { width: 1200px; height: 802px; overflow: hidden; background: var(--page); }
  .stage {
    position: relative; width: 960px; height: 642px;
    transform: scale(1.25); transform-origin: 0 0;
    font-family: "Comfortaa", "Century Gothic", sans-serif; color: var(--ink);
  }
  .banner { position: absolute; overflow: hidden; }
  .wood-bg {
    position: absolute; inset: 0;
    background:
      repeating-linear-gradient(90deg, rgba(255,255,255,.18) 0 3px, transparent 3px 11px, rgba(0,0,0,.06) 11px 13px, transparent 13px 19px),
      linear-gradient(90deg, var(--teal-light), var(--teal) 35%, var(--teal-light) 60%, var(--teal) 85%, var(--teal-light));
  }
  .frame {
    position: absolute; border: 9px solid var(--wood);
    border-image: linear-gradient(135deg, var(--wood-light), var(--wood), var(--wood-dark)) 1;
    box-shadow: 0 2px 6px rgba(0,0,0,.35);
  }
  .photo { position: absolute; }
  .photo-surf { background: linear-gradient(160deg, var(--sky) 0%, var(--sea) 45%, var(--white) 70%, var(--board) 100%); }
  .photo-beach { background: linear-gradient(180deg, var(--sky) 0%, #bcd7e0 28%, var(--sand) 45%, #f4efe4 100%); }
  .photo-strip { background: linear-gradient(90deg, var(--sea) 0%, var(--sky) 30%, var(--white) 55%, #bfe0ef 80%, var(--sky) 100%); }
  .badge { position: absolute; }
  .badge svg { display: block; width: 100%; height: 100%; }
  .badge-label {
    position: absolute; inset: 0; display: flex; align-items: center; justify-content: center;
    text-align: center; color: var(--white); font-family: "Fredoka", "Arial Black", sans-serif;
    font-weight: 600; line-height: .9; transform: rotate(-14deg);
  }
  .brand {
    position: absolute; display: flex; align-items: center; gap: 6px;
    font-family: "Comfortaa", sans-serif; font-weight: 400; color: var(--ink); line-height: 1;
  }
  .brand-dot { border-radius: 50%; background: var(--ink); flex: none; }
  .headline { position: absolute; font-weight: 700; line-height: 1.05; color: var(--ink); }
  .headline .big { font-size: 1.45em; }

  /* Skyscraper 160x600 */
  .skyscraper { left: 26px; top: 21px; width: 160px; height: 600px; }
  .skyscraper .headline { left: 0; right: 0; top: 20px; text-align: center; font-size: 19px; }
  .skyscraper .headline .big { display: block; font-size: 32px; line-height: 1.2; }

  /* Leaderboard 728x90 */
  .leaderboard { left: 222px; top: 43px; width: 728px; height: 90px; }
  .leaderboard .headline { left: 302px; top: 42px; font-size: 19px; white-space: nowrap; }
  .leaderboard .headline .big { font-size: 27px; }

  /* Large rectangle 336x280 */
  .rectangle { left: 222px; top: 163px; width: 336px; height: 280px; }
  .rectangle .headline { left: 126px; top: 62px; font-size: 25px; }
  .rectangle .headline .big { display: block; font-size: 40px; }

  /* Mobile leaderboard 320x50 */
  .mobile { left: 223px; top: 479px; width: 320px; height: 50px; }
  .mobile .headline { left: 164px; top: 26px; font-size: 11px; white-space: nowrap; }
</style>
</head>
<body>
<div class="stage">

  <!-- Skyscraper -->
  <section class="banner skyscraper" aria-label="Skyscraper banner">
    <div class="wood-bg" role="img" aria-label="Teal painted wood planks"></div>
    <div class="frame" style="left:6px; top:218px; width:170px; height:320px; transform:rotate(-2deg);"></div>
    <div class="photo photo-surf" role="img" aria-label="Young surfer riding a yellow board" style="left:44px; top:236px; width:120px; height:282px; transform:rotate(-2deg);"></div>
    <h2 class="headline">Improve your <span class="big">surfing skills</span></h2>
    <div class="badge" style="left:5px; top:148px; width:96px; height:96px;">
      <svg viewBox="0 0 100 100" aria-hidden="true"><circle cx="50" cy="50" r="47" fill="var(--badge)" stroke="var(--badge-edge)" stroke-width="3"/></svg>
      <span class="badge-label" style="font-size:22px;">JOIN<br>NOW!</span>
    </div>
    <div class="brand" style="left:14px; top:552px; font-size:17px; flex-direction:column; align-items:flex-start; gap:2px;">
      <span>Harbor</span><span>Retreats</span>
    </div>
    <span class="brand-dot" style="position:absolute; left:122px; top:556px; width:26px; height:26px; border-radius:50%; background:var(--ink);"></span>
  </section>

  <!-- Leaderboard -->
  <section class="banner leaderboard" aria-label="Leaderboard banner">
    <div class="wood-bg" role="img" aria-label="Teal painted wood planks"></div>
    <div class="photo photo-strip" role="img" aria-label="Young surfer on a yellow board beside snorkel goggles" style="left:222px; top:6px; width:506px; height:84px;"></div>
    <div class="frame" style="left:214px; top:-4px; width:520px; height:98px; transform:rotate(-1deg);"></div>
    <h2 class="headline">Improve your <span class="big">surfing skills</span></h2>
    <div class="brand" style="left:20px; top:22px; font-size:21px; flex-direction:column; align-items:flex-start; gap:3px;">
      <span>Harbor</span><span>Retreats</span>
    </div>
    <span class="brand-dot" style="position:absolute; left:150px; top:22px; width:44px; height:44px;"></span>
    <div class="badge" style="left:618px; top:3px; width:84px; height:84px;">
      <svg viewBox="0 0 100 100" aria-hidden="true"><circle cx="50" cy="50" r="47" fill="var(--badge)" stroke="var(--badge-edge)" stroke-width="3"/></svg>
      <span class="badge-label" style="font-size:20px;">JOIN<br>NOW!</span>
    </div>
  </section>

  <!-- Large rectangle -->
  <section class="banner rectangle" aria-label="Large rectangle banner">
    <div class="wood-bg" role="img" aria-label="Teal painted wood planks"></div>
    <div class="photo photo-beach" role="img" aria-label="Group of kids in rash guards running on the beach" style="left:58px; top:0; width:278px; height:168px;"></div>
    <div class="frame" style="left:40px; top:-20px; width:320px; height:196px; transform:rotate(-3deg);"></div>
    <h2 class="headline">make new <span class="big">Friends</span></h2>
    <div class="badge" style="left:18px; top:150px; width:100px; height:100px;">
      <svg viewBox="0 0 100 100" aria-hidden="true"><circle cx="50" cy="50" r="47" fill="var(--badge)" stroke="var(--badge-edge)" stroke-width="3"/></svg>
      <span class="badge-label" style="font-size:24px;">JOIN<br>NOW!</span>
    </div>
    <div class="brand" style="left:128px; top:212px; font-size:20px; flex-direction:column; align-items:flex-start; gap:3px;">
      <span>Harbor</span><span>Retreats</span>
    </div>
    <span class="brand-dot" style="position:absolute; left:254px; top:210px; width:44px; height:44px;"></span>
  </section>

  <!-- Mobile leaderboard -->
  <section class="banner mobile" aria-label="Mobile leaderboard banner">
    <div class="wood-bg" role="img" aria-label="Teal painted wood planks"></div>
    <div class="photo photo-strip" role="img" aria-label="Young surfer on a yellow board beside snorkel goggles" style="left:110px; top:3px; width:210px; height:47px;"></div>
    <div class="frame" style="left:104px; top:-4px; width:222px; height:58px; border-width:5px;"></div>
    <h2 class="headline">learn how to surf</h2>
    <div class="brand" style="left:6px; top:12px; font-size:11px; flex-direction:column; align-items:flex-start; gap:2px;">
      <span>Harbor</span><span>Retreats</span>
    </div>
    <span class="brand-dot" style="position:absolute; left:84px; top:12px; width:22px; height:22px;"></span>
    <div class="badge" style="left:276px; top:4px; width:42px; height:42px;">
      <svg viewBox="0 0 100 100" aria-hidden="true"><circle cx="50" cy="50" r="47" fill="var(--badge)" stroke="var(--badge-edge)" stroke-width="3"/></svg>
      <span class="badge-label" style="font-size:10px;">JOIN<br>NOW!</span>
    </div>
  </section>

</div>
</body>
</html>
```